Cedar nest sal
Affordable luxury
Professional
Paul dorsey
Doesn't matter, just write anything, will finalize later
Pauldorsey@quillmarsh.net
All I need is a template that suits the logo, I expect a draft template from your side.
It should include, the name, title, company logo, subtitle, website address, physical address, phone number and email. Thank you
Please suggest
Design number 1 will be used
red as second option

```html
<!DOCTYPE html>
<html lang="en">
<head>
<meta charset="UTF-8">
<title>Cedar Nest Sal – Business Card</title>
<link rel="stylesheet" href="https://fonts.googleapis.com/css2?family=Merriweather:ital,wght@0,400;0,700;1,700&display=swap">
<style>
  :root {
    --backdrop: #353535;
    --card-white: #ffffff;
    --leaf-green: #5f912b;
    --bark-brown: #6a3810;
    --text-light: #ffffff;
  }
  html, body {
    margin: 0;
    width: 1200px;
    height: 780px;
    overflow: hidden;
    background: var(--backdrop);
  }
  .card {
    position: absolute;
    left: 100px;
    top: 100px;
    width: 1000px;
    height: 580px;
    border-radius: 34px;
    overflow: hidden;
    background: var(--card-white);
    font-family: "Merriweather", Georgia, serif;
  }
  .card-shapes {
    position: absolute;
    inset: 0;
  }
  .person {
    position: absolute;
    left: 44px;
    top: 112px;
    color: var(--text-light);
  }
  .person-name {
    margin: 0;
    font-size: 30px;
    font-weight: 700;
    font-style: italic;
  }
  .person-title {
    margin: 6px 0 0;
    font-size: 22px;
  }
  .contact {
    position: absolute;
    left: 44px;
    top: 318px;
    color: var(--text-light);
    font-size: 19px;
    line-height: 1.45;
  }
  .contact-address {
    margin: 0 0 14px;
    font-style: normal;
  }
  .contact-list {
    list-style: none;
    margin: 0;
    padding: 0;
  }
  .contact-list li {
    display: flex;
    align-items: center;
    gap: 12px;
    height: 30px;
  }
  .contact-icon {
    width: 18px;
    height: 18px;
    flex: none;
  }
  .brand-name {
    position: absolute;
    left: 500px;
    top: 190px;
    width: 460px;
    margin: 0;
    text-align: center;
    font-size: 46px;
    font-weight: 400;
    color: var(--bark-brown);
  }
</style>
</head>
<body>
  <section class="card">
    <svg class="card-shapes" viewBox="0 0 1000 580" width="1000" height="580" aria-hidden="true">
      <path d="M0 0 H395 C375 130 470 320 715 580 H0 Z" fill="var(--leaf-green)"/>
      <path d="M395 0 H450 C405 120 480 310 728 580 H715 C470 320 375 130 395 0 Z" fill="var(--bark-brown)"/>
    </svg>

    <div class="person">
      <h1 class="person-name">Paul dorsey</h1>
      <p class="person-title">job title</p>
    </div>

    <div class="contact">
      <address class="contact-address">Suite 102 Street name,<br>State, Zip 2034,Country</address>
      <ul class="contact-list">
        <li>
          <svg class="contact-icon" viewBox="0 0 24 24"><path fill="#fff" d="M6.6 10.8a15 15 0 0 0 6.6 6.6l2.2-2.2c.3-.3.7-.4 1-.2 1.1.4 2.3.6 3.6.6.6 0 1 .4 1 1V20c0 .6-.4 1-1 1A17 17 0 0 1 3 4c0-.6.4-1 1-1h3.5c.6 0 1 .4 1 1 0 1.3.2 2.5.6 3.6.1.3 0 .7-.2 1z"/></svg>
          <span>127 555 0142</span>
        </li>
        <li>
          <svg class="contact-icon" viewBox="0 0 24 24"><rect x="6" y="2" width="12" height="20" rx="2" fill="#fff"/><rect x="8" y="5" width="8" height="11" fill="var(--leaf-green)"/></svg>
          <span>345 555 0187</span>
        </li>
        <li>
          <svg class="contact-icon" viewBox="0 0 24 24"><circle cx="12" cy="12" r="10" fill="#fff"/><text x="12" y="16.5" text-anchor="middle" font-size="13" font-family="Arial, sans-serif" font-weight="700" fill="var(--leaf-green)">@</text></svg>
          <span>Pauldorsey@quillmarsh.net</span>
        </li>
        <li>
          <svg class="contact-icon" viewBox="0 0 24 24" fill="none" stroke="#fff" stroke-width="2"><circle cx="12" cy="12" r="9.5"/><ellipse cx="12" cy="12" rx="4" ry="9.5"/><path d="M2.5 12h19"/></svg>
          <span>www.cedarnestsal.com</span>
        </li>
      </ul>
    </div>

    <p class="brand-name">Cedar Nest Sal</p>
  </section>
</body>
</html>
```